Design some Business Cards for Ferncrest Studio *UPDATE*

We would you to design a business card that is colourful and professional. Our business logo is attached in several formats.
The details we would like on the initial card are included below. Please note we will also supply the winner with the details of two other people and would like to have our winner include both of those people into the final design for us as well. The changes will just be different names and contact phone numbers etc.
We will be using standard business card dimensions with a high gloss finish.
The layout is ENTIRELY up to you!!! *UPDATE* - Office phone and fax number have been updated.
_________________________________________________________
Details on the front of card should include;
Martin Hobbes
Level 1, 217 Wexford Parade Street
Melbourne VIC 3000
ferncreststudio.com.au
Mobile: 0420 738 516
Office: +61 (0)3 9482 6031
Fax: +61 (0)3 9482 6354
Email: martin@ferncreststudio.com.au
__________________________________________________________
Back of the card - let your talent shine!!! We would like something eye catching.
It should include the FERNCREST STUDIO logo (please see attached files)
THANK YOU ALL AND GOOD LUCK

```html
<!DOCTYPE html>
<html lang="en">
<head>
<meta charset="utf-8">
<title>Ferncrest Studio – Business Cards</title>
<link href="https://fonts.googleapis.com/css2?family=Open+Sans:wght@400;600;700&display=swap" rel="stylesheet">
<style>
  :root {
    --bg: #2b2b2d;
    --brand-blue: #1a8fc9;
    --brand-blue-light: #37b3e6;
    --brand-blue-deep: #0f6fa6;
    --brand-green: #6b9a1f;
    --card-white: #ffffff;
    --card-grey: #e9e9e9;
    --text-grey: #555a5e;
    --rule: #c9cccf;
  }
  * { box-sizing: border-box; margin: 0; padding: 0; }
  html, body { width: 1200px; height: 900px; overflow: hidden; }
  body {
    background: var(--bg);
    font-family: "Open Sans", sans-serif;
    position: relative;
  }
  .card {
    position: absolute;
    left: 320px;
    width: 560px;
    height: 320px;
    border-radius: 2px;
    box-shadow: 0 10px 30px rgba(0,0,0,.45);
    overflow: hidden;
  }
  .card-back {
    top: 100px;
    background: radial-gradient(ellipse at 50% 45%, var(--brand-blue-light) 0%, var(--brand-blue) 55%, var(--brand-blue-deep) 100%);
    display: flex;
    flex-direction: column;
    align-items: center;
    justify-content: center;
    gap: 18px;
  }
  .back-mark {
    width: 64px; height: 64px; border-radius: 50%;
    background: var(--card-white);
  }
  .back-name {
    color: var(--card-white);
    font-weight: 700;
    font-size: 40px;
    letter-spacing: 1px;
  }
  .card-front {
    top: 480px;
    background: linear-gradient(160deg, var(--card-white) 0%, var(--card-white) 55%, var(--card-grey) 100%);
    padding: 26px 30px;
  }
  .front-logo { display: flex; align-items: center; gap: 12px; }
  .front-mark { width: 34px; height: 34px; border-radius: 50%; background: var(--brand-blue); }
  .front-name {
    color: var(--brand-blue);
    font-weight: 700;
    font-size: 24px;
    letter-spacing: .5px;
  }
  .rule { height: 1px; background: var(--rule); margin: 16px 0 14px; }
  .person { font-size: 28px; font-weight: 700; color: var(--brand-blue); line-height: 1.1; }
  .person .divider { color: var(--rule); font-weight: 400; margin: 0 6px; }
  .person .role { color: var(--brand-green); font-weight: 600; font-size: 24px; }
  .details {
    margin-top: 16px;
    display: grid;
    grid-template-columns: 150px 172px 1fr;
    column-gap: 10px;
    row-gap: 10px;
    font-size: 12.5px;
    color: var(--text-grey);
    white-space: nowrap;
  }
  .address { grid-column: 1 / 4; }
  .email { grid-column: 1 / 3; }
  .item { display: flex; align-items: center; gap: 8px; }
  .icon {
    width: 18px; height: 18px; border-radius: 3px;
    background: var(--brand-blue);
    display: flex; align-items: center; justify-content: center;
    flex: none;
  }
  .web { color: var(--brand-blue); font-weight: 700; }
</style>
</head>
<body>
  <section class="card card-back">
    <div class="back-mark"></div>
    <div class="back-name">FERNCREST STUDIO</div>
  </section>

  <section class="card card-front">
    <div class="front-logo">
      <div class="front-mark"></div>
      <div class="front-name">FERNCREST STUDIO</div>
    </div>
    <div class="rule"></div>
    <div class="person">Martin Hobbes<span class="divider">|</span><span class="role">Director</span></div>
    <div class="details">
      <div class="address">Level 1, 217 Wexford Parade Street Melbourne VIC 3000</div>
      <div class="item">
        <span class="icon"><svg width="10" height="12" viewBox="0 0 10 12"><rect x="1.5" y="0.5" width="7" height="11" rx="1.2" fill="none" stroke="#fff" stroke-width="1.2"/><circle cx="5" cy="9.3" r=".8" fill="#fff"/></svg></span>
        0420 738 516
      </div>
      <div class="item">
        <span class="icon"><svg width="12" height="12" viewBox="0 0 12 12"><path d="M2.5 1 L4.5 1 L5.3 3.6 L4 4.6 C4.8 6.3 5.7 7.2 7.4 8 L8.4 6.7 L11 7.5 L11 9.5 C11 10.4 10.3 11 9.4 11 C5 10.6 1.4 7 1 2.6 C1 1.7 1.6 1 2.5 1 Z" fill="#fff"/></svg></span>
        +61 (0)3 9482 6031
      </div>
      <div class="item">
        <span class="icon"><svg width="12" height="12" viewBox="0 0 12 12"><rect x="3" y="1" width="6" height="3" fill="none" stroke="#fff" stroke-width="1"/><rect x="1" y="4" width="10" height="5" rx="1" fill="#fff"/><rect x="3" y="8" width="6" height="3" fill="#fff" stroke="#1a8fc9" stroke-width=".8"/></svg></span>
        +61 (0)3 9482 6354
      </div>
      <div class="item email">
        <span class="icon"><svg width="12" height="12" viewBox="0 0 12 12"><circle cx="6" cy="6" r="2.2" fill="none" stroke="#fff" stroke-width="1.2"/><path d="M8.2 4v2.6c0 1.2 1.8 1.2 1.8 0V6A4 4 0 1 0 7.6 9.7" fill="none" stroke="#fff" stroke-width="1.2"/></svg></span>
        martin@ferncreststudio.com.au
      </div>
      <div class="item web">ferncreststudio.com.au</div>
    </div>
  </section>
</body>
</html>
```